Brosnick Antler Meadow Youth Hunt

We need to design a flyer for our upcoming inner city kids youth hunt . October 16-18th. It need to look similar to last years flyer which is attached. We use this flyer for our sponsors to get our supplies donated

Please include the additional Paper towels
Toilet paper 1-ply sheet
Brivex Wipes
Hand sanitizer
Sealwick bags gallon size
All purpose spray cleaner w/bleach
Pumarel spray
Fieldmorrow lemonade mix
Zolp mix
Quenchora powder mix
Tamblin water bottles-25
Granola bars
Chips
Pebblets
Crunvola
Peanut butter crackers
Trail mix
22 long rifle bullets
Latex gloves - M/ Lg
AA LED flashlights

Target Market(s)

Large Business and Donors

Font styles to use
Serif
Sans Serif

Requirements
Must have
• Must have Logos, and list of supplies
Nice to have
• Lots of colors and a great visual appeal for social media

```html
<!DOCTYPE html>
<html lang="en">
<head>
<meta charset="utf-8">
<title>Brosnick Antler Meadow Youth Hunt – Donation Flyer</title>
<link href="https://fonts.googleapis.com/css2?family=Montserrat:wght@400;600;700;800&display=swap" rel="stylesheet">
<style>
  :root {
    --sky-top: #b3def3;
    --sky-mid: #d3e2f4;
    --sky-low: #c4def5;
    --orange: #eb961f;
    --green: #22a34a;
    --ink: #2b2b2b;
    --ink-soft: #3a3a3a;
    --white: #ffffff;
    --rule: #b9c4d2;
    --grass: #8cc63f;
    --forest: #2f9e55;
  }
  * { box-sizing: border-box; margin: 0; padding: 0; }
  html, body { width: 901px; height: 1200px; overflow: hidden; background: #ffffff; }
  .flyer {
    position: relative; width: 901px; height: 1200px; overflow: hidden;
    font-family: "Montserrat", sans-serif; color: var(--ink);
    background: linear-gradient(180deg, var(--sky-top) 0%, var(--sky-mid) 30%, var(--sky-mid) 60%, var(--sky-low) 70%);
  }
  .presenters { position: absolute; left: 55px; top: 48px; font-size: 17px; line-height: 24px; color: var(--ink-soft); }
  .presenters strong { font-weight: 700; color: var(--ink); }
  .headline {
    position: absolute; left: 55px; top: 128px; width: 500px;
    font-weight: 800; font-size: 29.5px; line-height: 34px; color: var(--orange); letter-spacing: 0.2px;
  }
  .event-badge {
    position: absolute; left: 540px; top: -80px; width: 370px; height: 370px; border-radius: 50%;
    background: var(--white); border: 4px solid var(--green);
  }
  .event-badge__name {
    position: absolute; left: 60px; top: 150px; width: 230px; text-align: center;
    font-weight: 800; font-size: 24px; line-height: 30px; color: var(--ink); text-transform: uppercase;
  }
  .event-badge__year {
    position: absolute; left: 60px; top: 275px; width: 230px; text-align: center;
    font-weight: 600; font-size: 24px; color: var(--ink);
  }
  .sponsoring { position: absolute; left: 55px; top: 312px; font-size: 17px; line-height: 23px; color: var(--ink-soft); }
  .event-title {
    position: absolute; left: 55px; top: 361px; width: 406px;
    border-top: 1px solid var(--orange); border-bottom: 1px solid var(--orange);
    padding: 3px 0 2px; font-weight: 700; font-size: 20px; line-height: 25px; color: var(--orange); letter-spacing: 0.4px;
  }
  .venue { position: absolute; left: 55px; top: 428px; font-size: 17px; color: var(--ink-soft); }
  .intro { position: absolute; left: 55px; top: 467px; width: 460px; font-size: 14px; line-height: 18.5px; color: var(--ink-soft); }
  .intro strong { font-weight: 700; color: var(--ink); }
  .donation-box {
    position: absolute; left: 50px; top: 584px; width: 352px; height: 70px;
    border: 1px solid var(--green); border-radius: 8px; text-align: center;
  }
  .donation-box__label {
    position: absolute; left: 50%; top: -9px; transform: translateX(-50%);
    background: var(--sky-mid); padding: 0 12px; white-space: nowrap;
    font-weight: 700; font-size: 13.5px; color: var(--green);
  }
  .donation-box__address { margin-top: 20px; font-size: 13.5px; line-height: 20px; color: var(--ink-soft); }
  .sponsor-marks { position: absolute; left: 55px; top: 688px; display: flex; align-items: center; height: 54px; }
  .sponsor-mark { display: flex; align-items: center; gap: 8px; font-weight: 700; font-size: 15px; line-height: 17px; color: var(--ink); text-transform: uppercase; }
  .sponsor-mark__dot { width: 14px; height: 14px; border-radius: 50%; background: var(--ink); flex: none; }
  .sponsor-marks__divider { width: 1px; height: 54px; background: var(--rule); margin: 0 16px; }
  .column-divider { position: absolute; left: 550px; top: 380px; width: 1px; height: 330px; background: var(--rule); }
  .help-heading {
    position: absolute; left: 578px; top: 378px; width: 300px;
    font-weight: 700; font-size: 13.5px; line-height: 17px; color: var(--green);
  }
  .supply-list { position: absolute; left: 578px; top: 435px; list-style: none; font-size: 11.5px; line-height: 15.5px; color: var(--ink-soft); }
  .supply-list li { position: relative; padding-left: 14px; }
  .supply-list li::before { content: ""; position: absolute; left: 2px; top: 6px; width: 4px; height: 4px; border-radius: 50%; background: var(--green); }
  .thanks {
    position: absolute; left: 63px; top: 782px; width: 755px; height: 36px;
    border: 1px solid var(--orange); text-align: center;
    font-weight: 800; font-size: 21px; line-height: 34px; color: var(--orange); letter-spacing: 0.3px;
  }
  .scene {
    position: absolute; left: 0; top: 820px; width: 901px; height: 380px;
    background: linear-gradient(180deg, #e6eef6 0%, #c9a46a 30%, var(--forest) 45%, var(--grass) 75%, #a5cf4a 100%);
  }
</style>
</head>
<body>
<main class="flyer">
  <p class="presenters">
    <strong>Brosnick Antler Meadow,</strong><br>
    <strong>The Ostrander's,</strong> and<br>
    <strong>Urban Trail Youth</strong> Proudly Present...
  </p>

  <h1 class="headline">THE YOUTH ARE THE<br>FUTURE OF OUR NATION,<br>TOGETHER WE CAN<br>HELP THEM LEARN TO<br>APPRECIATE THE OUTDOORS!</h1>

  <div class="event-badge">
    <p class="event-badge__name">Brosnick Antler Meadow Youth Hunt</p>
    <p class="event-badge__year">2020</p>
  </div>

  <p class="sponsoring">Brosnick Antler Meadow, The Ostrander's,<br>and Urban Trail Youth will be sponsoring</p>

  <h2 class="event-title">THE ANNUAL YOUTH DEER HUNT<br>OCTOBER 16-18TH, 2020</h2>

  <p class="venue">at Brosnick Antler Meadow.</p>

  <p class="intro">We are looking forward to being able to provide both an <strong>educational and fun experience</strong> for all children. Over the weekend, we will educate our youth on the mechanics and sport of hunting. This year's event will host <strong>boys &amp; girls aged 6-14</strong> at the Brosnick Antler Meadow.</p>

  <div class="donation-box">
    <span class="donation-box__label">Please Send Donations to</span>
    <p class="donation-box__address">Brosnick Holdings LP , 482 Kettleby Lane<br>Corvane, TX. 75091</p>
  </div>

  <div class="sponsor-marks">
    <div class="sponsor-mark"><span class="sponsor-mark__dot"></span><span>Brosnick<br>Antler Meadow</span></div>
    <div class="sponsor-marks__divider"></div>
    <div class="sponsor-mark"><span>Urban Trail<br>Youth</span></div>
  </div>

  <div class="column-divider"></div>

  <h3 class="help-heading">ANYONE INTERESTED IN HELPING OUR CAUSE CAN DONATE GOODS OR SUPPORT MONETARILY.</h3>

  <ul class="supply-list">
    <li>Additional Paper towels</li>
    <li>Toilet paper 1-ply sheet</li>
    <li>Brivex Wipes</li>
    <li>Hand sanitizer</li>
    <li>Sealwick bags gallon size</li>
    <li>All purpose spray cleaner w/bleach</li>
    <li>Pumarel spray</li>
    <li>Fieldmorrow lemonade mix</li>
    <li>Zolp mix</li>
    <li>Quenchora powder mix</li>
    <li>Tamblin water bottles-25</li>
    <li>Granola bars</li>
    <li>Chips</li>
    <li>Pebblets</li>
    <li>Crunvola</li>
    <li>Peanut butter crackers</li>
    <li>Trail mix</li>
    <li>22 long rifle bullets</li>
    <li>Latex gloves - M/ Lg</li>
    <li>AA LED flashlights</li>
  </ul>

  <p class="thanks">WE GREATLY APPRECIATE YOUR GENEROSITY!</p>

  <div class="scene" role="img" aria-label="Cartoon outdoor scene: a young hunter aiming a rifle among pine trees and hills at sunset, with two deer on a green meadow"></div>
</main>
</body>
</html>
```